Freelancers in the field of IT security and IT service need a business card design

I need a business card design for my company. I am a freelancer and active in the area of IT security, IT support% 26 # 252; tung, consulting. I am not yet color-coded, but it should be a modern color that can also be used for a later website. The design should be innovation. Exude dynamism and reliability

Target Market(s)

IT security, IT solutions

Contact Information for Business Card

Firma: brunov-consulting, Inhaber: Lukas Brunov
Adresse: Lindenhof 4, D-73618 Musterbrunn
Telefon: +49 (0) 5137 640928
E-Mail Lukas.Brunov@brunov-consulting.example

```html
<!DOCTYPE html>
<html lang="de">
<head>
<meta charset="utf-8">
<title>brunov-consulting – Visitenkarte</title>
<link href="https://fonts.googleapis.com/css2?family=Roboto:wght@300;400;700&display=swap" rel="stylesheet">
<style>
  :root {
    --stage: #9b9b9b;
    --brand-blue: #0a16f2;
    --brand-blue-deep: #0610c8;
    --card-black: #050507;
    --network-glow: #0c1a7a;
    --ink-light: #ffffff;
  }
  html, body {
    margin: 0;
    padding: 0;
    overflow: hidden;
  }
  body {
    width: 1200px;
    height: 720px;
    background: var(--stage);
    font-family: "Roboto", Arial, sans-serif;
    position: relative;
  }
  .card {
    position: absolute;
    top: 192px;
    width: 520px;
    height: 336px;
    box-sizing: border-box;
    box-shadow: 0 10px 24px rgba(0,0,0,0.28);
    overflow: hidden;
  }
  .card--front {
    left: 60px;
    background: linear-gradient(135deg, var(--brand-blue) 0%, var(--brand-blue-deep) 100%);
    color: var(--ink-light);
  }
  .card--back {
    left: 620px;
    background: var(--card-black);
  }
  .wordmark {
    display: flex;
    align-items: center;
    gap: 10px;
  }
  .wordmark__dot {
    width: 26px;
    height: 26px;
    border-radius: 50%;
    border: 2.5px solid currentColor;
    box-sizing: border-box;
    flex: none;
  }
  .wordmark__name {
    font-weight: 300;
    letter-spacing: 1.5px;
    white-space: nowrap;
  }
  .card--front .wordmark {
    position: absolute;
    left: 34px;
    top: 38px;
  }
  .card--front .wordmark__name {
    font-size: 30px;
  }
  .contact {
    position: absolute;
    left: 214px;
    top: 176px;
  }
  .contact__name {
    font-size: 18px;
    font-weight: 700;
    margin: 0;
  }
  .contact__role {
    font-size: 13px;
    font-weight: 300;
    margin: 2px 0 12px;
  }
  .contact__list {
    display: grid;
    grid-template-columns: 22px auto;
    row-gap: 3px;
    margin: 0;
    font-size: 13px;
    font-weight: 300;
    white-space: nowrap;
  }
  .contact__list dt {
    font-weight: 700;
  }
  .contact__list dd {
    margin: 0;
  }
  .network-art {
    position: absolute;
    inset: 0;
    background:
      radial-gradient(ellipse at 30% 20%, var(--network-glow) 0%, transparent 45%),
      radial-gradient(ellipse at 75% 80%, var(--network-glow) 0%, transparent 40%);
    opacity: 0.55;
  }
  .card--back .wordmark {
    position: absolute;
    left: 0;
    right: 0;
    top: 146px;
    justify-content: center;
    color: var(--brand-blue);
  }
  .card--back .wordmark__name {
    font-size: 34px;
  }
  .card--back .wordmark__dot {
    width: 30px;
    height: 30px;
  }
</style>
</head>
<body>
  <section class="card card--front" aria-label="Vorderseite">
    <div class="wordmark">
      <span class="wordmark__dot"></span>
      <span class="wordmark__name">brunov-consulting</span>
    </div>
    <div class="contact">
      <p class="contact__name">Lukas Brunov</p>
      <p class="contact__role">Inhaber</p>
      <dl class="contact__list">
        <dt>A:</dt><dd>Lindenhof 4, D-73618 Musterbrunn</dd>
        <dt>T:</dt><dd>+49 (0) 5137 640928</dd>
        <dt>E:</dt><dd>Lukas.Brunov@brunov-consulting.example</dd>
        <dt>W:</dt><dd>brunov-consulting.example</dd>
      </dl>
    </div>
  </section>

  <section class="card card--back" aria-label="Rückseite">
    <div class="network-art" role="img" aria-label="Dezentes blaues Netzwerkmuster aus verbundenen Punkten auf schwarzem Grund"></div>
    <div class="wordmark">
      <span class="wordmark__dot"></span>
      <span class="wordmark__name">brunov-consulting</span>
    </div>
  </section>
</body>
</html>
```